New wine label design needed for exciting new wine business

A wine label design is required for a new wine production business based in Australia. This label will need to incorporate the business name 'Oleno-Cru'. We would like it to have a classic feel for a super premium wine and to reflect prestige. Colour suggestions may include a white background and the use of the colour red although we are open to any colors. This label must reflect a serious wine at a serious price. We want our design to attract attention and have a relevance that will stand the test of time!

Thanks to everyone who provided designs for our wine label. We have been very impressed by the calibre of designs! We will be making a decision very soon.

```html
<!DOCTYPE html>
<html lang="en">
<head>
<meta charset="utf-8">
<title>Oleno-Cru Cabernet Sauvignon Label</title>
<link href="https://fonts.googleapis.com/css2?family=Libre+Baskerville:wght@400;700&family=Tenor+Sans&family=Marcellus&display=swap" rel="stylesheet">
<style>
  :root {
    --page: #ffffff;
    --label: #ffffff;
    --label-edge: #9a9a9a;
    --ink: #2b2422;
    --brand: #3b302c;
    --wine-red: #d71f26;
    --grape: #8e1b22;
    --shadow: rgba(0, 0, 0, 0.38);
  }
  * { box-sizing: border-box; margin: 0; padding: 0; }
  html, body {
    width: 1200px;
    height: 848px;
    overflow: hidden;
    background: var(--page);
  }
  .canvas {
    position: relative;
    width: 1200px;
    height: 848px;
  }
  .label {
    position: absolute;
    left: 325px;
    top: 84px;
    width: 549px;
    height: 680px;
    background: var(--label);
    border: 1px solid var(--label-edge);
    box-shadow: 12px 14px 12px var(--shadow);
  }
  .brand {
    position: absolute;
    left: 0;
    right: 0;
    top: 200px;
    display: flex;
    align-items: center;
    justify-content: center;
    gap: 16px;
  }
  .brand-mark {
    width: 26px;
    height: 26px;
    border-radius: 50%;
    background: var(--grape);
  }
  .brand-name {
    font-family: "Libre Baskerville", Georgia, serif;
    font-weight: 700;
    font-size: 54px;
    letter-spacing: 1px;
    color: var(--brand);
  }
  .variety-band {
    position: absolute;
    left: 0;
    right: 0;
    top: 385px;
    height: 29px;
    background: var(--wine-red);
    display: flex;
    align-items: center;
    justify-content: center;
  }
  .variety {
    font-family: "Libre Baskerville", Georgia, serif;
    font-weight: 700;
    font-size: 25px;
    line-height: 1;
    color: var(--ink);
    margin-top: 4px;
  }
  .info {
    position: absolute;
    left: 0;
    right: 0;
    top: 578px;
    text-align: center;
    font-family: "Tenor Sans", "Marcellus", sans-serif;
    font-size: 17px;
    letter-spacing: 0.3px;
    color: var(--ink);
  }
  .volume {
    position: absolute;
    left: 0;
    right: 0;
    top: 612px;
    text-align: center;
    font-family: "Marcellus", "Tenor Sans", sans-serif;
    font-weight: 700;
    font-size: 30px;
    color: var(--wine-red);
    -webkit-text-stroke: 0.6px var(--wine-red);
  }
</style>
</head>
<body>
  <main class="canvas">
    <section class="label">
      <div class="brand">
        <span class="brand-mark" aria-hidden="true"></span>
        <span class="brand-name">Oleno-Cru</span>
      </div>
      <div class="variety-band">
        <span class="variety">Cabernet Sauvignon</span>
      </div>
      <p class="info">PLACE YOUR TEXT HERE</p>
      <p class="volume">0,75l</p>
    </section>
  </main>
</body>
</html>
```